corwin's pastel

We are a family business based in sydney introducing a common brazilian street food into sydney cafes and restaurants.
what we provide are pastels which is a thinly crust pie with assorted fillings
we mainly focus on supplying cafes and restaurants but we do sell privately.
We have had a few cafes ask to stock our cards due to customer request. except we don't have any!! hence why we need you. : )
I have attached an image of our pastels which is just to give you an idea of what they look like.
Updates
I have just seen all the designs and am impressed by some of your work. I will have to sit with my parter later today and will hopefully have some more constructive feedback and a decision soon.
Hello designers,
Hello designers,
Target Market(s)
cafe's and restaurants
Industry/Entity Type
Business
Contact Information for Business Card
Corwin's pastel
joaquim 0468217094
corwinspastel@fernmail.example

```html
<!DOCTYPE html>
<html lang="en">
<head>
<meta charset="utf-8">
<title>Corwin's pastel — Business Card</title>
<link rel="stylesheet" href="https://fonts.googleapis.com/css2?family=Coustard:wght@900&display=swap">
<style>
  :root {
    --backdrop: #bdbdbd;
    --card-white: #ffffff;
    --brand-red: #d12428;
    --brand-orange: #f0932b;
    --contact-orange: #f29a24;
    --name-white: #ffffff;
    --shadow: rgba(0, 0, 0, 0.28);
  }
  html, body {
    margin: 0;
    padding: 0;
    width: 1200px;
    height: 900px;
    overflow: hidden;
    background: var(--backdrop);
  }
  .canvas {
    position: relative;
    width: 1200px;
    height: 900px;
    display: flex;
    align-items: center;
    justify-content: center;
  }
  .business-card {
    position: relative;
    width: 880px;
    height: 560px;
    border-radius: 36px;
    overflow: hidden;
    background: var(--card-white);
    box-shadow: 0 18px 40px var(--shadow);
    font-family: "Coustard", Georgia, serif;
  }
  .card-swoosh {
    position: absolute;
    inset: 0;
    width: 880px;
    height: 560px;
  }
  .swoosh-red { fill: var(--brand-red); }
  .swoosh-orange { fill: var(--brand-orange); }

  .brand-lockup {
    position: absolute;
    left: 80px;
    top: 110px;
    display: flex;
    align-items: center;
    gap: 22px;
  }
  .brand-dot {
    width: 96px;
    height: 96px;
    border-radius: 50%;
    background: var(--brand-orange);
    flex: none;
  }
  .brand-name {
    margin: 0;
    color: var(--brand-red);
    font-weight: 900;
    font-size: 58px;
    line-height: 1.05;
  }

  .contact-block {
    position: absolute;
    right: 50px;
    top: 322px;
    text-align: right;
    font-weight: 900;
  }
  .contact-name {
    margin: 0 0 22px;
    color: var(--name-white);
    font-size: 44px;
    line-height: 1;
  }
  .contact-phone,
  .contact-email {
    margin: 0;
    color: var(--contact-orange);
    line-height: 1.2;
  }
  .contact-phone { font-size: 34px; }
  .contact-email { font-size: 26px; }
</style>
</head>
<body>
  <main class="canvas">
    <section class="business-card" aria-label="Corwin's pastel business card">
      <svg class="card-swoosh" viewBox="0 0 880 560" aria-hidden="true">
        <path class="swoosh-red" d="M0,560 L0,505 C190,390 480,335 690,292 C790,270 855,225 880,160 L880,560 Z"/>
        <path class="swoosh-orange" d="M440,335 C630,292 820,240 880,105 L880,148 C835,252 650,298 440,335 Z"/>
      </svg>

      <div class="brand-lockup">
        <span class="brand-dot" aria-hidden="true"></span>
        <h1 class="brand-name">Corwin's<br>pastel</h1>
      </div>

      <address class="contact-block">
        <p class="contact-name">Joaquim</p>
        <p class="contact-phone">0468217094</p>
        <p class="contact-email">corwinspastel@fernmail.example</p>
      </address>
    </section>
  </main>
</body>
</html>
```